Healthcare and Professional IT Services Company need a redesigned business card

We are a IT Services company that targets small medical practices and professional business such as Attorneys, Accounts, Architects etc. We want to communicate a professional yet friendly image using recent logo redesign here on Sketchforge. Like to see the colors blue and orange in the design. Must use the Copper Lantern Technology as displayed in the new logo - then also want to incorporate the fish logo as well.

Target Market(s)

Small medical and professional services

Industry/Entity Type

It Company

Contact Information for Business Card

The usual stuff, place for name address phone website. Also maybe our tagline which is "hooked on technology"

Requirements
Must have
• My new logo and the fish somewhere on the card

```html
<!DOCTYPE html>
<html lang="en">
<head>
<meta charset="utf-8">
<title>Copper Lantern Technology — Business Card</title>
<link rel="stylesheet" href="https://fonts.googleapis.com/css2?family=Crimson+Text:ital,wght@0,400;1,400&family=Lato:wght@400;700&display=swap">
<style>
  :root {
    --page: #ecebe8;
    --card-white: #ffffff;
    --card-black: #0b0b0c;
    --blue-deep: #1a73bf;
    --blue-mid: #2f95d3;
    --blue-light: #53b8e2;
    --brand-blue: #2c9bd6;
    --accent-orange: #f0962e;
    --ink: #1c1c1c;
    --on-blue: #ffffff;
  }
  * { box-sizing: border-box; margin: 0; padding: 0; }
  html, body { width: 1200px; height: 892px; overflow: hidden; }
  body {
    background: var(--page);
    display: flex;
    align-items: center;
    justify-content: center;
    gap: 56px;
    font-family: "Lato", sans-serif;
  }
  .card {
    position: relative;
    width: 540px;
    height: 309px;
    overflow: hidden;
    box-shadow: 0 6px 18px rgba(0,0,0,.18);
  }

  /* Front */
  .card--front { background: var(--card-white); }
  .contact-panel {
    position: absolute;
    left: 0; top: 0;
    width: 300px; height: 168px;
    background: linear-gradient(160deg, var(--blue-deep) 0%, var(--blue-mid) 55%, var(--blue-light) 100%);
    border-bottom-right-radius: 14px;
    padding: 18px 20px 0 24px;
    color: var(--on-blue);
  }
  .person-name {
    font-family: "Crimson Text", serif;
    font-size: 30px;
    font-weight: 400;
    text-align: right;
    letter-spacing: .5px;
    margin-bottom: 14px;
  }
  .contact-list { list-style: none; font-size: 12.5px; line-height: 1.45; }
  .contact-list li { display: flex; align-items: flex-start; gap: 7px; }
  .contact-list svg { flex: none; margin-top: 2px; }
  .contact-list .indent { padding-left: 18px; }
  .tagline {
    position: absolute;
    left: 24px; top: 196px;
    width: 340px;
    font-family: "Crimson Text", serif;
    font-size: 15px;
    white-space: nowrap;
    color: var(--ink);
  }

  .brand-lockup {
    display: flex;
    align-items: center;
    gap: 12px;
    color: var(--brand-blue);
    font-family: "Lato", sans-serif;
    font-weight: 700;
    line-height: 1.05;
  }
  .brand-mark {
    border-radius: 50%;
    background: var(--brand-blue);
    flex: none;
  }
  .brand-name { display: block; }
  .brand-rule {
    display: block;
    height: 3px;
    background: var(--accent-orange);
    margin-top: 8px;
    border-radius: 2px;
  }

  .card--front .brand-lockup {
    position: absolute;
    left: 318px; top: 62px;
    font-size: 20px;
  }
  .card--front .brand-mark { width: 34px; height: 34px; }
  .card--front .brand-rule { width: 86px; }

  .corner-tab {
    position: absolute;
    right: 0; bottom: 0;
    width: 170px; height: 70px;
    background: var(--blue-deep);
    border-top-left-radius: 14px;
  }

  /* Back */
  .card--back {
    background: var(--card-black);
    display: flex;
    align-items: center;
    justify-content: center;
  }
  .card--back .brand-lockup { font-size: 34px; gap: 16px; }
  .card--back .brand-mark { width: 48px; height: 48px; }
  .card--back .brand-rule { width: 140px; margin-top: 10px; }
</style>
</head>
<body>

  <section class="card card--front" aria-label="Business card front">
    <div class="contact-panel">
      <h1 class="person-name">Dana Whitfield</h1>
      <ul class="contact-list">
        <li>
          <svg width="11" height="11" viewBox="0 0 12 12" aria-hidden="true"><rect width="12" height="12" rx="2" fill="#fff"/><path d="M3.5 2.5c.6 0 1 1.3 1 1.7s-.7.6-.5 1.1c.4.9 1 1.5 1.8 1.8.5.2.7-.5 1.1-.5s1.7.4 1.7 1c0 .7-.8 1.4-1.6 1.4C5 9 3 7 2.6 4.1c0-.8.3-1.6.9-1.6z" fill="#1a73bf"/></svg>
          <span>480-555-0148</span>
        </li>
        <li>
          <svg width="11" height="11" viewBox="0 0 12 12" aria-hidden="true"><rect width="12" height="12" rx="2" fill="#fff"/><circle cx="6" cy="6" r="3.3" fill="none" stroke="#1a73bf" stroke-width="1.2"/><path d="M2.7 6h6.6M6 2.7c-1.4 2-1.4 4.6 0 6.6M6 2.7c1.4 2 1.4 4.6 0 6.6" fill="none" stroke="#1a73bf" stroke-width=".8"/></svg>
          <span>www.copperlantern.com</span>
        </li>
        <li>
          <svg width="11" height="11" viewBox="0 0 12 12" aria-hidden="true"><rect width="12" height="12" rx="2" fill="#fff"/><path d="M6 2.5 2.5 5.6h1v3.6h2V7h1v2.2h2V5.6h1z" fill="#1a73bf"/></svg>
          <span>2210 W.Harbor Lane tempe,</span>
        </li>
        <li class="indent">Arizona 85281</li>
      </ul>
    </div>

    <div class="brand-lockup">
      <span class="brand-mark" aria-hidden="true"></span>
      <span>
        <span class="brand-name">Copper Lantern<br>Technology</span>
        <span class="brand-rule" aria-hidden="true"></span>
      </span>
    </div>

    <p class="tagline">Also maybe our tagline which is "hooked on technology"</p>

    <div class="corner-tab"></div>
  </section>

  <section class="card card--back" aria-label="Business card back">
    <div class="brand-lockup">
      <span class="brand-mark" aria-hidden="true"></span>
      <span>
        <span class="brand-name">Copper Lantern<br>Technology</span>
        <span class="brand-rule" aria-hidden="true"></span>
      </span>
    </div>
  </section>

</body>
</html>
```